BrivoMatex. Lantern for the Steady Growth. Business card

Professional business card for BrivoMatex (Lantern for the Steady Growth)
My rationale: Strategy-> Execution-> Results-> Value that lead to the BrivoMatex name: We put the Lantern for the Steady Growth.
We deliver value to our customers helping them at defining a good strategy (cyan arrow). 90% of well formulated strategies fail due to poor execution so we also consider strategical execution very important (green arrow). Due to the execution we obtain the results (blue arrow). Finally, the results provide feedback to redefine strategy, and the new strategy has to be executed and new results obtained providing new feedback and on and on. It's like a wheel that finally, must create corporate value: value for shareholders, staholders, employees, providers...-

Target Market(s)

CEOs and steering comitees , invewrnent funds

Industry/Entity Type

Business Consultant

Contact Information for Business Card

Tommaso Ferlini
CEO & Founder
tommaso.ferlini@brivomatex.example
Mobile: +34 611.205.938
www.brivomatex.example

Colors

Designer to choose colors to be used in the design.

Requirements
Nice to have
• Nice to hace the words: Strategy, execution, results
• Nice to vave the claim: Lantern for the Steady Growth
• The three colors should be shown:
• cyan for STRATEGY
• green for EXECUTION
• blue for RESULTS
Should not have
• Complete black background

```html
<!DOCTYPE html>
<html lang="en">
<head>
<meta charset="utf-8">
<title>BrivoMatex Business Card</title>
<link rel="stylesheet" href="https://fonts.googleapis.com/css2?family=Lato:wght@400;700&display=swap">
<style>
  :root {
    --backdrop: #dddddd;
    --card: #ffffff;
    --navy: #253e8f;
    --green: #8cc63f;
    --cyan: #29abe2;
    --grey: #8c8c8c;
    --rule: #c8c8c8;
  }
  * { margin: 0; padding: 0; box-sizing: border-box; }
  html, body {
    width: 1200px;
    height: 960px;
    overflow: hidden;
    background: var(--backdrop);
    font-family: "Lato", "Helvetica Neue", Arial, sans-serif;
  }
  .card {
    position: absolute;
    left: 281px;
    width: 655px;
    height: 374px;
    background: var(--card);
    border-radius: 26px;
  }
  .card--front { top: 80px; }
  .card--back { top: 506px; }

  .brand-name {
    position: absolute;
    color: var(--navy);
    font-weight: 700;
    font-size: 46px;
    letter-spacing: -1px;
    line-height: 1;
    white-space: nowrap;
  }
  .card--front .brand-name {
    left: 55px;
    top: 135px;
  }
  .card--back .brand-name {
    left: 0;
    right: 0;
    text-align: center;
    top: 160px;
  }

  .divider {
    position: absolute;
    left: 293px;
    top: 118px;
    width: 1px;
    height: 138px;
    background: var(--rule);
  }
  .contact {
    position: absolute;
    left: 310px;
    top: 118px;
  }
  .contact__name {
    color: var(--navy);
    font-weight: 700;
    font-size: 27px;
    line-height: 1.1;
  }
  .contact__role {
    color: var(--grey);
    font-size: 17px;
    margin-top: 5px;
  }
  .contact__list {
    list-style: none;
    margin-top: 18px;
  }
  .contact__item {
    display: flex;
    align-items: center;
    gap: 8px;
    color: var(--grey);
    font-size: 17px;
    line-height: 24px;
  }
  .contact__icon {
    width: 14px;
    height: 14px;
    flex: none;
    fill: none;
    stroke: var(--navy);
  }

  .tagline {
    position: absolute;
    left: 0;
    right: 0;
    top: 282px;
    text-align: center;
    font-size: 18px;
    letter-spacing: 0.3px;
    color: var(--grey);
  }
  .tagline__strategy { color: var(--cyan); }
  .tagline__execution { color: var(--green); }
  .tagline__results { color: var(--navy); }
</style>
</head>
<body>
  <section class="card card--front">
    <div class="brand-name">BrivoMatex</div>
    <div class="divider"></div>
    <div class="contact">
      <div class="contact__name">Tommaso Ferlini</div>
      <div class="contact__role">CEO &amp; Founder</div>
      <ul class="contact__list">
        <li class="contact__item">
          <svg class="contact__icon" viewBox="0 0 14 14" aria-hidden="true">
            <path d="M3 13 C2 9 5 4 11 2 L12.5 3.5 L10.5 5.5 L9 4.5 C7 5.5 5 8 4.5 10.5 L6 11.5 L4.5 13.5 Z" fill="var(--navy)" stroke="none"/>
          </svg>
          <span>+34 611.205.938</span>
        </li>
        <li class="contact__item">
          <svg class="contact__icon" viewBox="0 0 14 14" aria-hidden="true">
            <rect x="1" y="3" width="12" height="8" fill="var(--navy)" stroke="none"/>
            <path d="M1 3 L7 8 L13 3" stroke="#fff" stroke-width="1.3"/>
          </svg>
          <span>tommaso.ferlini@brivomatex.example</span>
        </li>
        <li class="contact__item">
          <svg class="contact__icon" viewBox="0 0 14 14" aria-hidden="true" stroke-width="1.2">
            <circle cx="7" cy="7" r="5.8"/>
            <ellipse cx="7" cy="7" rx="2.6" ry="5.8"/>
            <path d="M1.2 7 H12.8 M2 4 H12 M2 10 H12"/>
          </svg>
          <span>www.brivomatex.example</span>
        </li>
      </ul>
    </div>
  </section>

  <section class="card card--back">
    <div class="brand-name">BrivoMatex</div>
    <p class="tagline">
      <span class="tagline__strategy">STRATEGY</span>
      -
      <span class="tagline__execution">EXECUTION</span>
      -
      <span class="tagline__results">RESULTS</span>
    </p>
  </section>
</body>
</html>
```